Stikers for GPS tracking company

I would like to have a sticker designed that my customers put on their vehicles and machines, to show that they have a Gps Tracking Alarm installed in their vehicle or machine.

Like stickers you use and put in your window in your home to show you have video surveillance system installed in your house.

It should be 10 cm high and 7 cm wide.

I have attached a version i have made myself, but im not satisfied with it

Target Market(s)

This is stickers that will sit on my customers assets, so the Volmira logo should be less visible and large,

Industry/Entity Type

GPS tracking and fleet management

Font styles to use
Sans Serif

Colors
0054AA
0677BA
7BADD7
CADEEF
E8F1F8

Requirements
Must have
• There should be an indication of location awareness

```html
<!DOCTYPE html>
<html lang="en">
<head>
<meta charset="utf-8">
<title>Volmira GPS Tracking Alarm Sticker</title>
<link rel="stylesheet" href="https://fonts.googleapis.com/css2?family=Exo+2:wght@700;900&display=swap">
<style>
  :root {
    --frame-blue: #1f9cec;
    --navy: #0c2a55;
    --navy-mid: #1d3f6e;
    --street-grey: #7c7f84;
    --accent-blue: #1f9cec;
    --white: #ffffff;
    --page: #ffffff;
  }
  html, body {
    margin: 0;
    padding: 0;
    width: 1200px;
    height: 1200px;
    overflow: hidden;
    background: var(--page);
  }
  .canvas {
    width: 1200px;
    height: 1200px;
    display: flex;
    align-items: center;
    justify-content: center;
  }
  .sticker {
    position: relative;
    width: 522px;
    height: 756px;
    border: 12px solid var(--frame-blue);
    background: linear-gradient(180deg, var(--navy) 0%, var(--navy) 38%, var(--navy-mid) 52%, var(--street-grey) 85%, var(--street-grey) 100%);
    overflow: hidden;
    font-family: "Exo 2", sans-serif;
  }
  .brand-band {
    height: 80px;
    background: var(--white);
    display: flex;
    align-items: center;
    justify-content: center;
    gap: 12px;
  }
  .brand-square {
    width: 32px;
    height: 32px;
    background: var(--accent-blue);
    border-radius: 3px;
  }
  .brand-name {
    font-weight: 700;
    font-size: 40px;
    color: var(--navy);
    letter-spacing: 1px;
  }
  .street-map {
    position: absolute;
    left: 0;
    right: 0;
    top: 380px;
    bottom: 0;
    background: linear-gradient(180deg, rgba(124,127,132,0) 0%, rgba(110,116,126,0.55) 45%, rgba(124,127,132,0.9) 100%);
  }
  .headline {
    position: relative;
    margin: 0;
    padding-top: 26px;
    text-align: center;
    font-weight: 900;
    font-size: 96px;
    line-height: 87px;
    letter-spacing: -1px;
    color: var(--white);
    text-transform: uppercase;
  }
  .headline span { display: block; }
  .headline .alarm { color: var(--accent-blue); }
  .location-pin {
    position: absolute;
    left: 50%;
    top: 450px;
    transform: translateX(-50%);
    width: 150px;
    height: 220px;
  }
</style>
</head>
<body>
<main class="canvas">
  <section class="sticker">
    <header class="brand-band">
      <div class="brand-square"></div>
      <span class="brand-name">Volmira</span>
    </header>
    <div class="street-map" role="img" aria-label="Grey street map of city roads behind the location marker"></div>
    <h1 class="headline">
      <span>GPS</span>
      <span>Tracking</span>
      <span class="alarm">Alarm</span>
    </h1>
    <svg class="location-pin" viewBox="0 0 150 220" aria-hidden="true">
      <path fill="#ffffff" fill-rule="evenodd" d="M75 4 C36 4 6 34 6 72 C6 112 40 150 75 214 C110 150 144 112 144 72 C144 34 114 4 75 4 Z M75 46 A27 27 0 1 0 75 100 A27 27 0 1 0 75 46 Z"/>
    </svg>
  </section>
</main>
</body>
</html>
```